drink bottle label

Our drink is called VELTRANA qa, a 2000 year old Asian formula for a fermented green tea drink. Flavored with organic ginger juice, cinnamon and lime. Very tasty and refreshing, good for sports recovery, digestion,liver detox,overall health and vitality. Naturally fermented creating a- no sugar, low GI, salt,-fat and gluten free- fizzy drink alternative to soft drink, sports drinks or beer. The bottle is a brown 330ml long neck bottle. For the diet and health conscious individual. We would like the label to be upmarket for restaurants & trendy organic food suppliers.
Updates

The bottle is brown. Try using black-gold-silver-white for the subject in a white or silver border

Target Market(s)

Upmarket, for restaurant & trendy organic food supplies.Sophisticated Health conscious people who don't want high sugar, caffeine drinks.

Industry/Entity Type

Health

Requirements
Must have
• The drink name and registered brand is" VELTRANA qa."
Must feature PROBIOTICS & ENZYMES for detox.No artificial preservatives or colours. 100% Organic & raw living culture.Low GI low calorie- no cane sugar, no salt-
- no lactose, Coeliac -diabetic & vegan friendly. Ginger Brew.
Nice to have
• tastes great-revitalize- 330ml brown bottle

```html
<!DOCTYPE html>
<html lang="en">
<head>
<meta charset="utf-8">
<title>Veltrana Max — Organic Ginger label</title>
<link href="https://fonts.googleapis.com/css2?family=Questrial&family=Titan+One&family=Arimo:wght@400;700&display=swap" rel="stylesheet">
<style>
  :root{
    --page:#eeeeee;
    --silver-a:#f4f4f4;
    --silver-b:#a9a9a9;
    --silver-c:#d6d6d6;
    --gold-a:#8a5a1c;
    --gold-b:#d9b77a;
    --gold-c:#f6ecc9;
    --pink-a:#e2185f;
    --pink-b:#f7a9c6;
    --pink-c:#fde6ef;
    --ink:#1e1e1e;
    --muted:#f7f7f7;
    --leaf:#2f6b1e;
    --yellow:#f7e61b;
    --white:#ffffff;
  }
  *{box-sizing:border-box;margin:0;padding:0}
  html,body{width:1200px;height:1000px;overflow:hidden;background:var(--page)}
  body{position:relative;font-family:"Questrial",sans-serif;color:var(--ink)}

  .label-slot{position:absolute;left:100px;width:1000px;height:464px}
  .label-slot.top{top:24px}
  .label-slot.bottom{top:512px}

  .label{
    position:absolute;left:0;top:0;width:708px;height:328px;
    transform:scale(1.4124);transform-origin:0 0;
    background:linear-gradient(90deg,var(--silver-a) 0%,var(--silver-b) 30%,var(--silver-c) 55%,var(--silver-b) 80%,var(--silver-a) 100%);
    overflow:hidden;
  }
  .label.gold{--band:linear-gradient(90deg,var(--gold-a),var(--gold-b) 30%,var(--gold-c) 55%,var(--gold-b) 75%,var(--gold-a));--ring:#b98a3e}
  .label.pink{--band:linear-gradient(90deg,var(--pink-c),var(--pink-b) 25%,var(--pink-a) 50%,var(--pink-b) 75%,var(--pink-c));--ring:#e0427c}

  .top-band{position:absolute;left:0;top:0;width:100%;height:10px;background:var(--band)}
  .base-band{position:absolute;left:0;top:237px;width:100%;height:91px;background:var(--band)}

  .story{position:absolute;left:15px;top:48px;width:82px;font-size:6.3px;line-height:1.55;color:var(--muted)}

  .claim{
    position:absolute;left:117px;width:60px;height:60px;border-radius:50%;
    background:var(--white);border:3px solid var(--ring);
    display:flex;align-items:center;justify-content:center;text-align:center;
    font-family:"Arimo",sans-serif;font-weight:700;font-size:7.4px;line-height:1.2;color:var(--leaf);
  }
  .claim.c1{top:28px}.claim.c2{top:98px}.claim.c3{top:163px}

  .hero-art{position:absolute;left:238px;top:18px;width:225px;height:190px}
  .brand-name{
    position:absolute;left:232px;top:94px;width:240px;text-align:center;
    font-family:"Questrial",sans-serif;font-size:34px;color:var(--leaf);letter-spacing:1px;line-height:1;
  }
  .volume{position:absolute;left:400px;top:202px;font-size:7.5px;font-family:"Arimo",sans-serif}
  .suitability{position:absolute;left:230px;top:220px;width:220px;text-align:center;font-family:"Arimo",sans-serif;font-weight:700;font-size:12.5px}

  .nutrition{
    position:absolute;left:525px;top:25px;width:131px;height:196px;background:var(--white);
    padding:4px 5px;font-family:"Arimo",sans-serif;font-size:6.2px;line-height:1.38;color:#333;
  }
  .nutrition h3{font-size:7px;font-weight:700;border-bottom:2px solid #333;padding-bottom:1px}
  .nutrition .row{display:flex;justify-content:space-between;border-bottom:.5px solid #999}
  .nutrition .in{padding-left:8px}
  .nutrition .thick{border-bottom:2px solid #333}
  .nutrition b{font-weight:700}
  .nutrition .foot{margin-top:4px;font-size:5.8px;line-height:1.3}

  .distributed{position:absolute;left:15px;top:246px;font-size:6.5px;color:var(--muted)}
  .free-from{position:absolute;left:175px;top:244px;width:330px;text-align:center;font-family:"Arimo",sans-serif;font-weight:700;font-size:9.6px;white-space:nowrap}
  .low{position:absolute;left:175px;top:259px;width:330px;text-align:center;font-family:"Arimo",sans-serif;font-weight:700;font-size:8.5px}
  .flavour{
    position:absolute;left:175px;top:280px;width:330px;text-align:center;
    font-family:"Titan One",sans-serif;font-size:22px;color:var(--yellow);letter-spacing:.5px;
    text-shadow:-1px -1px 0 #4a3310,1px -1px 0 #4a3310,-1px 1px 0 #4a3310,2px 2px 0 #4a3310;
  }
  .recycle{position:absolute;left:600px;top:243px;width:40px;height:14px}
</style>
</head>
<body>

<div class="label-slot top">
  <section class="label gold">
    <div class="top-band"></div>
    <div class="base-band"></div>
    <p class="story">Our drink is called VELTRANA qa, a 2000 year old Asian formula for a fermented green tea drink. Flavored with organic ginger juice, cinnamon and lime. Very tasty and refreshing, good for sports recovery, digestion, liver detox, overall health and vitality. Naturally fermented creating a - no sugar, low GI, salt, fat and gluten free- fizzy drink alternative to soft drink, sports drinks or beer.</p>
    <div class="claim c1">Probiotics<br>&amp; Enzymes<br>For<br>inner health</div>
    <div class="claim c2">No artificial<br>preservatives<br>or colours</div>
    <div class="claim c3">Glucaric<br>Acid<br>for detox</div>
    <svg class="hero-art" role="img" aria-label="Illustration of a lime juice splash with tea leaves, lime slice, cinnamon and ginger root" viewBox="0 0 225 190"><defs><radialGradient id="splashGold" cx="45%" cy="40%" r="60%"><stop offset="0" stop-color="#f3ee8a"/><stop offset=".7" stop-color="#c9c64a" stop-opacity=".75"/><stop offset="1" stop-color="#c9c64a" stop-opacity="0"/></radialGradient></defs><ellipse cx="105" cy="90" rx="105" ry="92" fill="url(#splashGold)"/></svg>
    <div class="brand-name">Veltrana Max</div>
    <div class="volume">330ml</div>
    <div class="suitability">Coeliac☑ Diabetic☑ Vegan☑</div>
    <div class="nutrition">
      <h3>Nutrition Facts</h3>
      <div>Serving Size 1/2 Cup (85g)</div>
      <div class="thick">Serving Per Container About 4</div>
      <div>Amount Per Serving</div>
      <div class="row"><span><b>Calories</b> 160</span><span><b>Calories from Fat</b> 120</span></div>
      <div class="row" style="justify-content:flex-end">% Daily Value*</div>
      <div class="row"><span><b>Total Fat</b> 9g</span><span>14%</span></div>
      <div class="row in"><span>Saturated Fat 5g</span><span>25%</span></div>
      <div class="row in"><span>Trans Fat 0g</span><span></span></div>
      <div class="row in"><span>Cholesterol 30mg</span><span>10%</span></div>
      <div class="row in"><span>Sodium 30mg</span><span>1%</span></div>
      <div class="row"><span><b>Total Carbohydrate</b> 18g</span><span>6%</span></div>
      <div class="row"><span>Dietary Fiber 0g</span><span>0%</span></div>
      <div class="row"><span>Sugars 16g</span><span></span></div>
      <div class="row thick"><span><b>Protein</b> 2g</span><span></span></div>
      <div class="row"><span>VitaminA 6%</span><span>• VitaminC 2%</span></div>
      <div class="row thick"><span>Calcium 6%</span><span>• Iron 0%</span></div>
      <p class="foot">* Percent Daily Values are based on a 2,000 calorie diet.</p>
    </div>
    <div class="distributed">Distributed by:</div>
    <div class="free-from">☒No Cane Sugar ☒No Salt ☒No Lactose ☒No Glucose ☒No Gluten</div>
    <div class="low">Low Calorie, Low GI</div>
    <div class="flavour">Organic Ginger</div>
    <svg class="recycle" viewBox="0 0 40 14" aria-label="Recycle and dispose icons"><path d="M4 11 L8 4 L12 11 Z" fill="none" stroke="#fff" stroke-width="1.3"/><rect x="27" y="5" width="5" height="8" fill="none" stroke="#fff" stroke-width="1.2"/><circle cx="34" cy="2.5" r="1.5" fill="#fff"/><path d="M34 4 V9" stroke="#fff" stroke-width="1.2"/></svg>
  </section>
</div>

<div class="label-slot bottom">
  <section class="label pink">
    <div class="top-band"></div>
    <div class="base-band"></div>
    <p class="story">Our drink is called VELTRANA qa, a 2000 year old Asian formula for a fermented green tea drink. Flavored with organic ginger juice, cinnamon and lime. Very tasty and refreshing, good for sports recovery, digestion, liver detox, overall health and vitality. Naturally fermented creating a - no sugar, low GI, salt, fat and gluten free- fizzy drink alternative to soft drink, sports drinks or beer.</p>
    <div class="claim c1">Probiotics<br>&amp; Enzymes<br>For<br>inner health</div>
    <div class="claim c2">No artificial<br>preservatives<br>or colours</div>
    <div class="claim c3">Glucaric<br>Acid<br>for detox</div>
    <svg class="hero-art" role="img" aria-label="Illustration of a lime juice splash with tea leaves, lime slice, cinnamon and ginger root" viewBox="0 0 225 190"><defs><radialGradient id="splashPink" cx="45%" cy="40%" r="60%"><stop offset="0" stop-color="#f3ee8a"/><stop offset=".7" stop-color="#c9c64a" stop-opacity=".75"/><stop offset="1" stop-color="#c9c64a" stop-opacity="0"/></radialGradient></defs><ellipse cx="105" cy="90" rx="105" ry="92" fill="url(#splashPink)"/></svg>
    <div class="brand-name">Veltrana Max</div>
    <div class="volume">330ml</div>
    <div class="suitability">Coeliac☑ Diabetic☑ Vegan☑</div>
    <div class="nutrition">
      <h3>Nutrition Facts</h3>
      <div>Serving Size 1/2 Cup (85g)</div>
      <div class="thick">Serving Per Container About 4</div>
      <div>Amount Per Serving</div>
      <div class="row"><span><b>Calories</b> 160</span><span><b>Calories from Fat</b> 120</span></div>
      <div class="row" style="justify-content:flex-end">% Daily Value*</div>
      <div class="row"><span><b>Total Fat</b> 9g</span><span>14%</span></div>
      <div class="row in"><span>Saturated Fat 5g</span><span>25%</span></div>
      <div class="row in"><span>Trans Fat 0g</span><span></span></div>
      <div class="row in"><span>Cholesterol 30mg</span><span>10%</span></div>
      <div class="row in"><span>Sodium 30mg</span><span>1%</span></div>
      <div class="row"><span><b>Total Carbohydrate</b> 18g</span><span>6%</span></div>
      <div class="row"><span>Dietary Fiber 0g</span><span>0%</span></div>
      <div class="row"><span>Sugars 16g</span><span></span></div>
      <div class="row thick"><span><b>Protein</b> 2g</span><span></span></div>
      <div class="row"><span>VitaminA 6%</span><span>• VitaminC 2%</span></div>
      <div class="row thick"><span>Calcium 6%</span><span>• Iron 0%</span></div>
      <p class="foot">* Percent Daily Values are based on a 2,000 calorie diet.</p>
    </div>
    <div class="distributed">Distributed by:</div>
    <div class="free-from">☒No Cane Sugar ☒No Salt ☒No Lactose ☒No Glucose ☒No Gluten</div>
    <div class="low">Low Calorie, Low GI</div>
    <div class="flavour">Organic Ginger</div>
    <svg class="recycle" viewBox="0 0 40 14" aria-label="Recycle and dispose icons"><path d="M4 11 L8 4 L12 11 Z" fill="none" stroke="#fff" stroke-width="1.3"/><rect x="27" y="5" width="5" height="8" fill="none" stroke="#fff" stroke-width="1.2"/><circle cx="34" cy="2.5" r="1.5" fill="#fff"/><path d="M34 4 V9" stroke="#fff" stroke-width="1.2"/></svg>
  </section>
</div>

</body>
</html>
```